Portfolio site - Need a basic WordPress or SquareSpace site

I need a portfolio site where I have the option to keep updating it on my own. Therefore, I'm guessing I need one that uses WordPress or SquareSpace. I just need a simple and elegant design. I'm a writer (scholarly, fiction and journalism).

Target Market(s)

Adult

Industry/Entity Type

Writer

Number of Pages Required

4 page

Font styles to use
Serif

Colors
b7a5cd
e667a6
85abd2

Requirements
Must have
• Easily updatable features. I'll have to publish links and small blurbs from time to time. And maybe the occasional image.
• Pages should be:
• Home
• Work
• Press
• Contact

```html
<!DOCTYPE html>
<html lang="en">
<head>
<meta charset="utf-8">
<title>Mariam Qadir — Writer</title>
<link href="https://fonts.googleapis.com/css2?family=Arimo:ital,wght@0,400;0,700;1,400&family=Special+Elite&display=swap" rel="stylesheet">
<style>
  :root {
    --page-bg: #f4f4f4;
    --card-bg: #ffffff;
    --ink: #111111;
    --ink-soft: #333333;
    --muted: #8a8a8a;
    --rule: #b9b9b9;
    --field-border: #9a9a9a;
    --button-bg: #cdcdcd;
  }
  * { box-sizing: border-box; margin: 0; padding: 0; }
  html, body { width: 1200px; height: 2300px; overflow: hidden; }
  body {
    position: relative;
    background: var(--page-bg);
    color: var(--ink);
    font-family: "Arimo", Arial, sans-serif;
  }

  /* Header */
  .brand {
    position: absolute; top: 74px; left: 0; width: 1200px;
    text-align: center;
  }
  .brand-name {
    font-family: "Special Elite", "Courier New", monospace;
    font-size: 30px; letter-spacing: 1px; color: var(--ink);
  }
  .brand-tagline {
    display: block; margin-top: 2px; margin-left: 250px;
    font-family: "Special Elite", "Courier New", monospace;
    font-size: 9px; color: var(--ink-soft);
  }
  .main-nav {
    position: absolute; top: 183px; left: 412px; width: 376px; height: 50px;
    border-top: 2px solid var(--rule); border-bottom: 1px solid var(--rule);
    display: flex; align-items: center; justify-content: center; gap: 18px;
    font-size: 13px; font-weight: 700;
  }
  .main-nav a { color: var(--ink); text-decoration: none; }
  .main-nav .sep { font-weight: 400; }

  /* Work cards */
  .card {
    position: absolute; width: 305px;
    background: var(--card-bg); border-radius: 9px; overflow: hidden;
    text-align: center;
  }
  .card-image { display: block; width: 100%; }
  .card-title {
    margin: 22px 28px 0; font-size: 18px; font-weight: 700; line-height: 23px;
  }
  .card-excerpt {
    margin: 20px 34px 0; font-size: 13px; font-style: italic; line-height: 18px;
    color: var(--ink-soft);
  }
  .card-link {
    display: block; margin-top: 20px; font-size: 16px; color: var(--ink);
    text-decoration: none;
  }
  .col-1 { left: 122px; }
  .col-2 { left: 448px; }
  .col-3 { left: 773px; }

  .more-projects {
    position: absolute; top: 1519px; left: 0; width: 1200px; text-align: center;
    font-size: 13px; font-weight: 700; color: var(--ink); text-decoration: none;
  }

  /* Contact */
  .contact {
    position: absolute; left: 122px; top: 1605px; width: 956px; height: 476px;
    background: var(--card-bg); border-radius: 9px;
  }
  .contact-title {
    position: absolute; top: 27px; width: 100%; text-align: center;
    font-size: 16px; font-weight: 700;
  }
  .field {
    position: absolute; left: 51px; width: 852px; height: 42px;
    border: 1px solid var(--field-border); border-radius: 8px;
    padding-top: 18px; text-align: center;
    font-size: 13px; font-style: italic; color: var(--muted);
  }
  .field-message { height: 135px; padding-top: 6px; }
  .submit {
    position: absolute; left: 372px; top: 415px; width: 212px; height: 42px;
    background: var(--button-bg); border-radius: 6px;
    display: flex; align-items: center; justify-content: center;
    font-size: 15px; font-weight: 700; letter-spacing: 0.5px; color: var(--ink);
  }

  /* Footer */
  .site-footer {
    position: absolute; left: 0; top: 2123px; width: 1200px; height: 177px;
    border-top: 2px solid #cfcfcf;
  }
  .footer-col { position: absolute; top: 45px; }
  .footer-col h3 { font-size: 15px; font-weight: 700; margin-bottom: 7px; }
  .footer-col li {
    list-style: none; font-size: 11px; line-height: 14px; color: var(--ink-soft);
  }
</style>
</head>
<body>

<header>
  <div class="brand">
    <span class="brand-name">Mariam Qadir</span>
    <span class="brand-tagline">writer and comics scholar</span>
  </div>
  <nav class="main-nav">
    <a href="#">HOME</a><span class="sep">-</span>
    <a href="#">WORK</a><span class="sep">-</span>
    <a href="#">PRESS</a><span class="sep">-</span>
    <a href="#">CONTACT</a>
  </nav>
</header>

<main>
  <article class="card col-1" style="top:298px;height:516px;">
    <svg class="card-image" width="305" height="258" role="img" aria-label="Photo of a woman in glasses typing on a vintage typewriter"><rect width="305" height="258" fill="#cfcac4"/></svg>
    <h2 class="card-title">Lorem ipsum dolor sit amet, consectetuer adipiscing elit, sed diam</h2>
    <p class="card-excerpt">Lorem ipsum dolor sit amet, con-sectetuer adipiscing elit, sed diam nonummy nibh euismod tincidunt ut laoreet dolore magna aliquam erat volutpat. Ut wisi</p>
    <a class="card-link" href="#">See more</a>
  </article>

  <article class="card col-1" style="top:836px;height:653px;">
    <svg class="card-image" width="305" height="355" role="img" aria-label="Photo of a hand holding a cigarette over a typewriter against wood panelling"><defs><linearGradient id="wood" x1="0" y1="0" x2="1" y2="1"><stop offset="0" stop-color="#8a5f2e"/><stop offset="1" stop-color="#c39a5d"/></linearGradient></defs><rect width="305" height="355" fill="url(#wood)"/></svg>
    <h2 class="card-title">Lorem ipsum dolor sit amet, consectetuer adipiscing elit, sed diam</h2>
    <p class="card-excerpt">Lorem ipsum dolor sit amet, con-sectetuer adipiscing elit, sed diam nonummy nibh euismod tincidunt ut laoreet dolore magna aliquam erat volutpat. Ut wisi</p>
    <a class="card-link" href="#">See more</a>
  </article>

  <article class="card col-2" style="top:298px;height:654px;">
    <svg class="card-image" width="305" height="353" role="img" aria-label="Photo of a writer at a desk with a typewriter and wall calendar"><defs><linearGradient id="desk" x1="0" y1="0" x2="0" y2="1"><stop offset="0" stop-color="#6f8f7d"/><stop offset="0.75" stop-color="#7d9384"/><stop offset="1" stop-color="#b08a6e"/></linearGradient></defs><rect width="305" height="353" fill="url(#desk)"/></svg>
    <h2 class="card-title">Lorem ipsum dolor sit amet, consectetuer adipiscing elit, sed diam</h2>
    <p class="card-excerpt">Lorem ipsum dolor sit amet, con-sectetuer adipiscing elit, sed diam nonummy nibh euismod tincidunt ut laoreet dolore magna aliquam erat volutpat. Ut wisi</p>
    <a class="card-link" href="#">See more</a>
  </article>

  <article class="card col-2" style="top:972px;height:517px;">
    <svg class="card-image" width="305" height="258" role="img" aria-label="Book cover in grey tones"><defs><linearGradient id="cover" x1="0" y1="0" x2="0" y2="1"><stop offset="0" stop-color="#555555"/><stop offset="1" stop-color="#2e2e2e"/></linearGradient></defs><rect width="305" height="258" fill="url(#cover)"/></svg>
    <h2 class="card-title" style="margin-top:14px;">Lorem ipsum dolor sit amet, consectetuer adipiscing elit, sed diam</h2>
    <p class="card-excerpt">Lorem ipsum dolor sit amet, con-sectetuer adipiscing elit, sed diam nonummy nibh euismod tincidunt ut laoreet dolore magna aliquam erat volutpat. Ut wisi</p>
    <a class="card-link" href="#">See more</a>
  </article>

  <article class="card col-3" style="top:298px;height:516px;">
    <svg class="card-image" width="305" height="183" role="img" aria-label="Sepia photo of a child with a toy beside a typewriter"><rect width="305" height="183" fill="#b8a683"/></svg>
    <h2 class="card-title">Lorem ipsum dolor sit amet, consectetuer adipiscing elit, sed diam</h2>
    <p class="card-excerpt">Lorem ipsum dolor sit amet, con-sectetuer adipiscing elit, sed diam nonummy nibh euismod tincidunt ut laoreet dolore magna aliquam erat volutpat. Ut wisi</p>
    <a class="card-link" href="#">See more</a>
  </article>

  <article class="card col-3" style="top:836px;height:516px;">
    <svg class="card-image" width="305" height="184" role="img" aria-label="Black and white photo of a woman writing a letter at a table"><rect width="305" height="184" fill="#8e8b86"/></svg>
    <h2 class="card-title">Lorem ipsum dolor sit amet, consectetuer adipiscing elit, sed diam</h2>
    <p class="card-excerpt">Lorem ipsum dolor sit amet, con-sectetuer adipiscing elit, sed diam nonummy nibh euismod tincidunt ut laoreet dolore magna aliquam erat volutpat. Ut wisi</p>
    <a class="card-link" href="#">See more</a>
  </article>

  <a class="more-projects" href="#">more projects --&gt;</a>

  <section class="contact">
    <h2 class="contact-title">Contact Us</h2>
    <div class="field" style="top:82px;">name</div>
    <div class="field" style="top:140px;">email</div>
    <div class="field" style="top:198px;">subject</div>
    <div class="field field-message" style="top:257px;">message</div>
    <div class="submit">SUBMIT</div>
  </section>
</main>

<footer class="site-footer">
  <div class="footer-col" style="left:430px;">
    <h3>Info</h3>
    <ul><li>Stocklist</li><li>Lorem Ip</li><li>Ipsum dol</li><li>Privacy Policy</li><li>Terms &amp; Cond.</li></ul>
  </div>
  <div class="footer-col" style="left:533px;">
    <h3>Menu</h3>
    <ul><li>Home</li><li>Work</li><li>Press</li><li>Contact us</li></ul>
  </div>
  <div class="footer-col" style="left:628px;">
    <h3>Links</h3>
    <ul><li>Link 1</li><li>Link 2</li><li>Link 3</li><li>Link 4</li></ul>
  </div>
  <div class="footer-col" style="left:719px;">
    <h3>Social</h3>
    <ul><li>Friendbook</li><li>Chirper</li><li>Snapgram</li><li>ViewTube</li></ul>
  </div>
</footer>

</body>
</html>
```